Business Card Design and Basic Text Logo

We are looking for a business card design for an e-business company. Our business is the parent company of a few website businesses. The final logo and business card design will communicate a conservative but modern and expansive business

The Logo text is: 87Merchant
We would also like a basic text logo design for 87Merchant. The logo could also fill up the reverse side of the business card.

The colours we would like to use are:
White
Navy
Black

This is the text that will be added to the card:

Dean Colley
Business Development Manager

Phone: +61 417 658 294
Email: dean.colley@87merchant.com.au

Industry/Entity Type

Business

Logo Text

87Merchant

Logo styles of interest
Pictorial/Combination Logo
Requirements
Must have
• Modern and attractive design
Nice to have
• communicate a conservative but modern and expansive business
Should not have
• Should be too dull and plan
• But also should be overly colourful

```html
<!DOCTYPE html>
<html lang="en">
<head>
<meta charset="utf-8">
<title>87Merchant — Business Card</title>
<link rel="stylesheet" href="https://fonts.googleapis.com/css2?family=Arimo:wght@400;700&family=Roboto+Condensed:wght@300;400&display=swap">
<style>
  :root {
    --page: #ffffff;
    --bar: #231f20;
    --bar-text: #d9d9d9;
    --navy: #1a4474;
    --navy-deep: #102c52;
    --navy-light: #2f5d93;
    --black: #0a0a0a;
    --ink: #1b1b1b;
    --white: #ffffff;
    --label: #a8a8a8;
  }
  * { margin: 0; padding: 0; box-sizing: border-box; }
  html, body { width: 1200px; height: 900px; overflow: hidden; background: var(--page); }
  .sheet { position: relative; width: 1200px; height: 900px; font-family: "Roboto Condensed", "Arial Narrow", sans-serif; }

  .header-bar { position: absolute; top: 82px; height: 28px; background: var(--bar); color: var(--bar-text);
    font-size: 11px; font-weight: 300; display: flex; align-items: center; }
  .header-bar--left { left: 28px; width: 116px; }
  .header-bar--title { left: 147px; width: 788px; justify-content: center; text-transform: uppercase; }
  .header-bar--client { left: 938px; width: 230px; justify-content: flex-end; padding-right: 31px; }

  .column-label, .row-label { position: absolute; font-size: 10px; color: var(--label); font-weight: 300; }

  .card { position: absolute; width: 230px; height: 135px; overflow: hidden;
    box-shadow: 2px 3px 5px rgba(0,0,0,0.35); }
  .card--front { left: 331px; background: var(--white); border: 1px solid #e2e2e2; }
  .card--back { left: 616px; display: flex; align-items: center; justify-content: center; }
  .card--navy { background: radial-gradient(ellipse at center, var(--navy-light) 0%, var(--navy) 55%, var(--navy-deep) 100%); }
  .card--black { background: var(--black); }
  .row-1 { top: 232px; } .row-2 { top: 423px; } .row-3 { top: 616px; }

  .wordmark { font-family: "Arimo", Arial, sans-serif; font-weight: 700; letter-spacing: -0.3px; white-space: nowrap; }
  .wordmark--front { position: absolute; color: var(--navy); font-size: 14px; }
  .wordmark--header { color: var(--white); font-size: 14px; }
  .wordmark--back { color: var(--white); font-size: 24px; }

  .contact { position: absolute; right: 14px; text-align: right; color: var(--navy); line-height: 1.3; white-space: nowrap; }
  .contact__name { font-family: "Arimo", Arial, sans-serif; font-weight: 700; font-size: 12px; display: block; position: relative; }
  .contact__name--caps { font-weight: 400; font-size: 9px; letter-spacing: 1.6px; text-transform: uppercase; }
  .contact__rule { position: absolute; height: 1px; background: currentColor; }
  .contact__line { display: block; font-size: 8px; }

  .decor-circle { position: absolute; left: -70px; top: -10px; width: 150px; height: 150px; border-radius: 50%; background: var(--navy); }
  .title-band { position: absolute; left: 95px; right: 0; top: 74px; height: 15px; background: var(--navy);
    color: var(--white); font-size: 8px; text-align: right; padding-right: 14px; line-height: 15px; }

  .top-band { position: absolute; left: 0; right: 0; top: 0; height: 57px; background: var(--bar); }
</style>
</head>
<body>
<main class="sheet">
  <div class="header-bar header-bar--left"></div>
  <div class="header-bar header-bar--title">Business Card</div>
  <div class="header-bar header-bar--client">87Merchant</div>

  <span class="column-label" style="left:443px; top:157px;">A</span>
  <span class="column-label" style="left:725px; top:157px;">B</span>
  <span class="row-label" style="left:244px; top:291px;">1</span>
  <span class="row-label" style="left:244px; top:481px;">2</span>
  <span class="row-label" style="left:244px; top:676px;">3</span>

  <!-- Row 1 -->
  <section class="card card--front row-1">
    <span class="wordmark wordmark--front" style="left:10px; top:70px;">87Merchant</span>
    <div class="contact" style="top:54px;">
      <span class="contact__name">Dean Colley<span class="contact__rule" style="right:78px; width:30px; bottom:3px;"></span></span>
      <span class="contact__line">Business Development Manager</span>
      <span class="contact__line">+61 417 658 294</span>
      <span class="contact__line">dean.colley@87merchant.com.au</span>
    </div>
  </section>
  <section class="card card--back card--navy row-1">
    <span class="wordmark wordmark--back">87Merchant</span>
  </section>

  <!-- Row 2 -->
  <section class="card card--front row-2">
    <div class="decor-circle" aria-hidden="true"></div>
    <div class="contact" style="top:61px;">
      <span class="contact__name contact__name--caps">Dean Colley</span>
    </div>
    <div class="title-band">Business Development Manager</div>
    <div class="contact" style="top:91px;">
      <span class="contact__line">+61 417 658 294</span>
      <span class="contact__line">dean.colley@87merchant.com.au</span>
    </div>
  </section>
  <section class="card card--back card--navy row-2">
    <span class="wordmark wordmark--back">87Merchant</span>
  </section>

  <!-- Row 3 -->
  <section class="card card--front row-3">
    <div class="top-band"></div>
    <span class="wordmark wordmark--front wordmark--header" style="left:11px; top:20px;">87Merchant</span>
    <div class="contact" style="top:74px; right:10px; color:var(--ink);">
      <span class="contact__name contact__name--caps" style="font-size:10px;">Dean Colley<span class="contact__rule" style="right:110px; width:30px; bottom:2px;"></span></span>
      <span class="contact__line" style="font-size:9px;">Business Development Manager</span>
      <span class="contact__line" style="font-size:9px;">+61 417 658 294</span>
      <span class="contact__line" style="font-size:9px;">dean.colley@87merchant.com.au</span>
    </div>
  </section>
  <section class="card card--back card--black row-3">
    <span class="wordmark wordmark--back">87Merchant</span>
  </section>
</main>
</body>
</html>
```